New Business Card Design Project

double sided business cards. i would like to design a business card with the logo attached . that logo being centered on 1 side and then my info on the other.

Wesley Brandt CEO
Phone# 334-617-2054
Wesley@fairoakhomecare.example

Contact Information for Business Card

double sided one side the Logo attached below that saying Home Maintenance and Repair Specialists then on back my info Wesley Brandt CEO Home Maintenance Specialist Phone# 334-617-2054 Wesley@fairoakhomecare.example

Font styles to use
Serif

Colors
0054AA
0677BA
7BADD7
CADEEF
E8F1F8
FFC000
F8CF3A
FAE287
FDF2CF
FEFAEE

Requirements
Must have
• double sided logo attached on one side with colors blue and gold. black background info on the other side

```html
<!DOCTYPE html>
<html lang="en">
<head>
<meta charset="utf-8">
<title>Fair Oak Home Care – Business Card Revision</title>
<link rel="stylesheet" href="https://fonts.googleapis.com/css2?family=Poppins:wght@400;500&family=Mulish:wght@600;700;800&display=swap">
<style>
  :root {
    --card-black: #121011;
    --brand-blue: #2373be;
    --brand-gold: #fdbe12;
    --text-white: #ffffff;
    --rule-grey: #d9d9d9;
    --header-ink: #141414;
    --board-top: #d8d8d8;
    --board-mid: #efeeef;
    --board-bottom: #bdbcbd;
  }
  * { box-sizing: border-box; margin: 0; padding: 0; }
  html, body { width: 1200px; height: 1200px; overflow: hidden; }
  body {
    position: relative;
    background: linear-gradient(180deg, var(--board-top) 10%, var(--board-mid) 45%, var(--board-mid) 60%, var(--board-bottom) 100%);
    font-family: "Mulish", sans-serif;
  }
  .board-header {
    position: absolute; left: 3px; top: 0; width: 1197px; height: 121px;
    background: #fff; border-left: 1px solid #555; border-bottom: 1px solid #555;
    display: flex; align-items: center; justify-content: center;
  }
  .board-title {
    font-family: "Poppins", sans-serif; font-weight: 400; font-size: 39px;
    color: var(--header-ink); letter-spacing: 0.3px; margin-top: -8px;
  }
  .board-specs {
    position: absolute; top: 131px; left: 0; width: 100%; text-align: center;
    font-family: "Poppins", sans-serif; font-weight: 500; font-size: 22px; color: var(--header-ink);
  }
  .card {
    position: absolute; background: var(--card-black); color: var(--text-white);
  }
  .card--front { left: 200px; top: 205px; width: 791px; height: 437px; }
  .card--back  { left: 196px; top: 691px; width: 800px; height: 440px; }

  .brand-mark {
    position: absolute; left: 0; width: 100%;
    display: flex; flex-direction: column; align-items: center;
  }
  .card--front .brand-mark { top: 118px; gap: 22px; }
  .card--back .brand-mark { top: 40px; gap: 12px; }
  .brand-square { background: var(--brand-gold); }
  .card--front .brand-square { width: 64px; height: 64px; }
  .card--back .brand-square { width: 40px; height: 40px; }
  .brand-name {
    font-weight: 800; color: var(--brand-blue); letter-spacing: 2px; white-space: nowrap;
  }
  .card--front .brand-name { font-size: 50px; }
  .card--back .brand-name { font-size: 34px; }

  .holder {
    position: absolute; top: 190px; left: 0; width: 100%; text-align: center;
  }
  .holder-name { font-weight: 700; font-size: 47px; line-height: 1; letter-spacing: 0.5px; }
  .holder-role { font-size: 30px; font-weight: 700; }
  .holder-title {
    margin-top: 10px; font-weight: 600; font-size: 24px; color: var(--brand-gold); letter-spacing: 0.6px;
  }
  .contact-strip {
    position: absolute; left: 0; top: 307px; width: 100%; height: 98px;
    border-top: 1.5px solid var(--rule-grey); border-bottom: 1.5px solid var(--rule-grey);
    display: grid; grid-template-columns: 347px 1fr;
  }
  .contact-item {
    display: flex; flex-direction: column; align-items: center; justify-content: flex-start;
    padding-top: 12px; gap: 14px;
  }
  .contact-item + .contact-item { border-left: 1.5px solid var(--rule-grey); }
  .contact-icon { width: 32px; height: 32px; }
  .contact-text { font-weight: 600; font-size: 20px; letter-spacing: 0.4px; }
</style>
</head>
<body>
  <header class="board-header"><h1 class="board-title">Revision of old Design</h1></header>
  <p class="board-specs">100% Editable &nbsp;|&nbsp; Print Ready &nbsp;|&nbsp; CMYK Color Mode &nbsp;|&nbsp; 3.5in X 2.0 in</p>

  <section class="card card--front">
    <div class="brand-mark">
      <span class="brand-square"></span>
      <span class="brand-name">FAIR OAK HOME CARE</span>
    </div>
  </section>

  <section class="card card--back">
    <div class="brand-mark">
      <span class="brand-square"></span>
      <span class="brand-name">FAIR OAK HOME CARE</span>
    </div>
    <div class="holder">
      <p class="holder-name">Wesley Brandt-<span class="holder-role">CEO</span></p>
      <p class="holder-title">Maintenance and Repair Specialist</p>
    </div>
    <div class="contact-strip">
      <div class="contact-item">
        <svg class="contact-icon" viewBox="0 0 32 32" fill="none" stroke="#fdbe12" stroke-width="2" stroke-linejoin="round">
          <path d="M4 11c0-4 24-4 24 0v2h-6v-3H10v3H4z"/>
          <path d="M9 14h14l3 14H6z"/>
          <g fill="#fdbe12" stroke="none">
            <circle cx="13" cy="19" r="1.2"/><circle cx="16" cy="19" r="1.2"/><circle cx="19" cy="19" r="1.2"/>
            <circle cx="13" cy="22.5" r="1.2"/><circle cx="16" cy="22.5" r="1.2"/><circle cx="19" cy="22.5" r="1.2"/>
          </g>
        </svg>
        <span class="contact-text">334-617-2054</span>
      </div>
      <div class="contact-item">
        <svg class="contact-icon" viewBox="0 0 32 32" fill="none" stroke="#fdbe12" stroke-width="2" stroke-linejoin="round" stroke-linecap="round">
          <path d="M12 12l9-7 9 11-9 7z"/>
          <path d="M12 12l9 4 9 0"/>
          <path d="M3 13h6M1 17h7M4 21h6"/>
        </svg>
        <span class="contact-text">Wesley@fairoakhomecare.example</span>
      </div>
    </div>
  </section>
</body>
</html>
```